Online Sports Booking Business

We need a flyer design for a new company based in Bahrain called "GoalSlotter.com".

GoalSlotter is an online booking service for the sport field in Bahrain. We would like to design a flyer in away that reflects our idea and the type of customers who will benefit from the service. You can visit the website in order to get an idea about the service provided.

Service Description:
Simply sign up, search and choose, book and pay for any sports venue or activity using your own computer or smartphone.

- Choose from different sport centers and activities in Bahrain
- Compare based on unbiased reviews by real people
- Check for availability
- Book and pay online in less than a minute
- Track, manage, modify and cancel your bookings online
- Receive automatic notifications (upon request) whenever your favorite venue/activity is available
- Rate and post reviews about your experience

We would like the design to use the color green as a background, nice and casual visual icons and images to show the above steps. The final design should communicate the value and benefits in a joyful and casual way that is attractive to the sport lovers.
Updates

Project Deadline Extended
Reason: I need interested designers to take part in this project.

Target Market(s)

english speakers aged 18-45 who are into sports.

Industry/Entity Type

Computer

Font styles to use
Sans Serif
Other font styles liked:
• something similar to the logo

Colors
add136
9bcb3c
ffffff

Requirements
Must have
• Please use the content in the attachment. Logo can be taken from goalslotter.example
Nice to have
• steps and benefits to use icons and visual presentations rather than dull text only.

```html
<!DOCTYPE html>
<html lang="en">
<head>
<meta charset="utf-8">
<title>GoalSlotter.com Flyer</title>
<link rel="stylesheet" href="https://fonts.googleapis.com/css2?family=Russo+One&family=Lato:wght@400;700&family=Oswald:wght@400&display=swap">
<style>
  :root {
    --canvas-bg: #2b2b2b;
    --lime: #add136;
    --lime-mid: #9bcb3c;
    --green-deep: #3d5a16;
    --green-dark: #4a6b1e;
    --green-band: #6a9a25;
    --navy: #1c2a44;
    --gold: #a8822f;
    --line: #5d6a55;
    --white: #ffffff;
    --paper: #f4f5f2;
  }
  html, body {
    margin: 0;
    width: 902px;
    height: 1200px;
    overflow: hidden;
    background: var(--canvas-bg);
  }
  .flyer {
    position: absolute;
    left: 58px;
    top: 48px;
    width: 785px;
    height: 1100px;
    background: var(--paper);
    overflow: hidden;
    font-family: "Lato", sans-serif;
  }
  .flyer p, .flyer h1, .flyer h2 { margin: 0; }
  .hero-photo {
    position: absolute;
    left: 0; top: 0;
    width: 785px; height: 520px;
    background:
      radial-gradient(ellipse at 50% 12%, #e8f2ff 0%, #6f9ccc 22%, rgba(20,50,90,0) 55%),
      radial-gradient(ellipse at 45% 72%, #b8702e 0%, rgba(184,112,46,0) 28%),
      linear-gradient(180deg, #0f2748 0%, #1d4c7c 40%, #14335a 62%, #2e6a2a 80%, #3f7f2a 100%);
  }
  .waves {
    position: absolute;
    left: 0; top: 0;
    width: 785px; height: 1100px;
  }
  .brand-box {
    position: absolute;
    left: 17px; top: 7px;
    width: 225px; height: 103px;
    background: var(--green-band);
    display: flex;
    align-items: center;
    justify-content: center;
  }
  .brand-name {
    color: var(--white);
    font-weight: 700;
    font-size: 22px;
  }
  .headline {
    position: absolute;
    left: 0; top: 120px;
    width: 785px;
    text-align: center;
    font-family: "Russo One", sans-serif;
    font-weight: 400;
    font-variant: small-caps;
    font-size: 68px;
    line-height: 1;
    color: var(--lime);
    text-shadow: 0 3px 4px rgba(0,0,0,0.6);
  }
  .hero-url {
    position: absolute;
    left: 0; top: 196px;
    width: 785px;
    text-align: center;
    font-family: "Russo One", sans-serif;
    font-size: 32px;
    color: var(--white);
    text-shadow: 0 2px 4px rgba(0,0,0,0.6);
  }
  .free-badge {
    position: absolute;
    left: 386px; top: 370px;
    width: 184px; height: 184px;
    border-radius: 50%;
    background: radial-gradient(circle at 40% 35%, #ffffff 0%, #e6e8e2 70%, #c9ccc4 100%);
    box-shadow: 0 0 0 5px #d7dad2, 0 4px 10px rgba(0,0,0,0.35);
    display: flex;
    flex-direction: column;
    align-items: center;
    justify-content: center;
    font-family: "Oswald", sans-serif;
    font-weight: 400;
    font-size: 64px;
    line-height: 1;
    color: var(--green-dark);
  }
  .game-on {
    position: absolute;
    left: 226px; top: 598px;
    width: 470px;
    text-align: center;
    font-family: "Russo One", sans-serif;
    font-weight: 400;
    text-transform: uppercase;
    font-size: 84px;
    line-height: 1;
    color: var(--green-deep);
  }
  .click-line {
    position: absolute;
    left: 0; top: 696px;
    width: 785px;
    text-align: center;
    font-weight: 700;
    font-size: 28px;
    color: var(--navy);
  }
  .site-name {
    position: absolute;
    left: 0; top: 768px;
    width: 785px;
    text-align: center;
    font-family: "Russo One", sans-serif;
    font-weight: 400;
    text-transform: uppercase;
    font-size: 68px;
    line-height: 1;
    color: var(--lime-mid);
    text-shadow: 0 1px 0 var(--green-dark);
  }
  .tagline {
    position: absolute;
    left: 0; top: 850px;
    width: 785px;
    text-align: center;
    font-weight: 700;
    font-size: 21px;
    color: #3b5418;
  }
  .steps {
    position: absolute;
    left: 32px; top: 898px;
    width: 713px;
    border-top: 2px solid var(--gold);
    border-bottom: 2px solid var(--gold);
    padding: 6px 0 6px;
    text-align: center;
    font-family: "Oswald", sans-serif;
    font-weight: 400;
    font-size: 25px;
    line-height: 42px;
    color: var(--gold);
  }
  .contact-bar {
    position: absolute;
    left: 0; top: 1014px;
    width: 785px; height: 86px;
    background: var(--green-band);
    display: flex;
    justify-content: space-between;
    align-items: center;
    padding: 0 42px 0 34px;
    box-sizing: border-box;
    font-family: "Oswald", sans-serif;
    font-weight: 400;
    font-size: 30px;
    color: var(--white);
  }
  .contact-item { display: flex; align-items: center; gap: 10px; }
  .contact-item svg { fill: var(--white); }
</style>
</head>
<body>
  <main class="flyer">
    <div class="hero-photo" role="img" aria-label="Floodlit stadium with a basketball, football, soccer ball, volleyball and tennis ball on the grass"></div>

    <svg class="waves" viewBox="0 0 785 1100" aria-hidden="true">
      <defs>
        <linearGradient id="waveGreen" x1="0" y1="0" x2="1" y2="0">
          <stop offset="0" stop-color="#9bcb3c"/>
          <stop offset="1" stop-color="#add136"/>
        </linearGradient>
      </defs>
      <path d="M0 415 C150 468 300 472 420 440 C560 400 680 348 785 345 L785 1100 L0 1100 Z" fill="url(#waveGreen)"/>
      <path d="M0 462 C150 492 300 498 440 490 C580 482 700 512 785 560 L785 1100 L0 1100 Z" fill="#ffffff"/>
      <path d="M0 500 C250 520 500 520 785 578 L785 1100 L0 1100 Z" fill="url(#waveGreen)"/>
      <path d="M0 632 C90 628 200 598 360 578 C520 556 660 560 785 690 L785 1100 L0 1100 Z" fill="#f4f5f2"/>
      <path d="M0 500 C250 520 500 520 785 578" fill="none" stroke="#5d6a55" stroke-width="3"/>
    </svg>

    <div class="brand-box">
      <span class="brand-name">GoalSlotter.com</span>
    </div>

    <h1 class="headline">Pick your Pitch NOW</h1>
    <p class="hero-url">at goalslotter.example</p>

    <div class="free-badge"><span>IT’S</span><span>FREE</span></div>

    <h2 class="game-on">Game on!</h2>
    <p class="click-line">A click away from your favorite sports venue</p>

    <h2 class="site-name">GoalSlotter.com</h2>
    <p class="tagline">The place where you can instantly reserve your sport activity</p>

    <p class="steps">Simply sign up, search and choose, book and pay for any sports<br>venue or activity using your own computer or smartphone.</p>

    <footer class="contact-bar">
      <span class="contact-item">
        <svg width="26" height="28" viewBox="0 0 24 24" aria-hidden="true"><path d="M6.6 10.8c1.4 2.8 3.8 5.1 6.6 6.6l2.2-2.2c.3-.3.7-.4 1-.2 1.1.4 2.3.6 3.6.6.6 0 1 .4 1 1V20c0 .6-.4 1-1 1C10.6 21 3 13.4 3 4c0-.6.4-1 1-1h3.5c.6 0 1 .4 1 1 0 1.3.2 2.5.6 3.6.1.3 0 .7-.2 1z"/></svg>
        +973-30005566
      </span>
      <span class="contact-item">
        <svg width="28" height="20" viewBox="0 0 28 20" aria-hidden="true"><path d="M0 0h28v20H0z M2 2v1l12 8 12-8V2z" fill-rule="evenodd"/></svg>
        support@goalslotter.example
      </span>
    </footer>
  </main>
</body>
</html>
```